Business Card Design Project

I am looking for a business card design for my custom Audio/Video & Contracting business named Brindlemoor Systems Inc. We do not currently have a corporate logo so you should not feel constrained to work around an existing design. Your design should be elegant and clean while artistically conveying that we are a technology company. We provide A/V services for the commercial and residential markets and contracting services for residential remodeling and home theater construction. We do not have a particular color that we are looking to design around so feel free to be creative.

To get references of the kind of work that we do and design inspiration please visit the following sites:

http://www.velqorant.us
www.pelmotrix.com
www.quillharborinc.com

Reason: I think we are getting close on a couple of the designs and want to give additional time to get tweaks done and to resubmit your designs.

Target Market(s)

Most of our clients are very wealthy and have been exposed to premium brand names in every aspect of their lives, (ie. - luxury autos, estate sized homes, fine jewelery and clothes) and your design needs to convey that same level of excellent design that they are used to.

Industry/Entity Type

Residential

Requirements
Should not have
• An extensive use of the color RED.

```html
<!DOCTYPE html>
<html lang="en">
<head>
<meta charset="utf-8">
<title>Brindlemoor Systems – Business Cards</title>
<link rel="stylesheet" href="https://fonts.googleapis.com/css2?family=Signika:wght@400;600;700&display=swap">
<style>
  :root {
    --backdrop: #2b2a29;
    --paper: #ffffff;
    --brand-green: #6cb33f;
    --brand-blue: #343b9c;
    --ink-blue: #2f3590;
    --card-w: 540px;
    --card-h: 308px;
  }
  * { box-sizing: border-box; margin: 0; padding: 0; }
  html, body {
    width: 1200px;
    height: 900px;
    overflow: hidden;
    background: var(--backdrop);
    font-family: "Signika", "Trebuchet MS", sans-serif;
  }
  .sheet { position: relative; width: 1200px; height: 900px; }

  .card {
    position: absolute;
    width: var(--card-w);
    height: var(--card-h);
    overflow: hidden;
    box-shadow: 0 10px 24px rgba(0,0,0,0.45);
  }
  .card--front { left: 80px; top: 80px; background: var(--paper); }
  .card--green { left: 600px; top: 250px; background: var(--brand-green); }
  .card--blue  { left: 80px; top: 510px; background: var(--brand-blue); }

  /* Front card */
  .holder { position: absolute; right: 34px; top: 30px; text-align: right; }
  .holder__name { color: var(--ink-blue); font-size: 22px; font-weight: 400; line-height: 1.2; }
  .holder__title { color: var(--brand-green); font-size: 15px; font-weight: 400; margin-top: 2px; }

  .wordmark {
    position: absolute;
    display: flex;
    align-items: center;
    gap: 12px;
    font-weight: 700;
    letter-spacing: 0.02em;
    line-height: 1;
  }
  .wordmark__dot { width: 14px; height: 14px; border-radius: 50%; flex: none; }
  .card--front .wordmark { left: 30px; top: 110px; font-size: 34px; color: var(--brand-green); }
  .card--front .wordmark__dot { background: var(--brand-green); }

  .contact {
    position: absolute;
    right: 34px;
    top: 160px;
    text-align: right;
    list-style: none;
    color: var(--ink-blue);
    font-size: 13.5px;
    line-height: 1.42;
  }

  .edge-band { position: absolute; left: 0; bottom: 0; width: 100%; height: 42px; }

  /* Colour backs */
  .card--green .wordmark,
  .card--blue .wordmark {
    left: 0; right: 0; top: 112px;
    justify-content: center;
    font-size: 44px;
    color: var(--paper);
  }
  .card--green .wordmark__dot,
  .card--blue .wordmark__dot { background: var(--paper); width: 18px; height: 18px; }

  .web {
    position: absolute;
    left: 0; right: 0; bottom: 42px;
    text-align: center;
    color: var(--paper);
    font-size: 16px;
    font-weight: 400;
    letter-spacing: 0.01em;
  }
</style>
</head>
<body>
<main class="sheet">

  <section class="card card--front" aria-label="Business card front">
    <div class="holder">
      <p class="holder__name">Daniel Ashworth</p>
      <p class="holder__title">Marketing Manager</p>
    </div>

    <div class="wordmark">
      <span class="wordmark__dot"></span>
      <span class="wordmark__name">Brindlemoor Systems</span>
    </div>

    <ul class="contact">
      <li>48 N. Harlow Crest</li>
      <li>Emberton, NW 52318</li>
      <li>Tel.: (555) 318-2046</li>
      <li>Fax: (555) 318-2047</li>
      <li>info@brindlemoor-systems.com</li>
    </ul>

    <svg class="edge-band" viewBox="0 0 540 42" preserveAspectRatio="none" aria-hidden="true">
      <path d="M0 22 C150 28 330 30 540 14 L540 42 L0 42 Z" fill="var(--brand-green)"/>
      <path d="M0 31 C160 34 340 34 540 24 L540 42 L0 42 Z" fill="var(--brand-blue)"/>
    </svg>
  </section>

  <section class="card card--green" aria-label="Business card back, green">
    <div class="wordmark">
      <span class="wordmark__dot"></span>
      <span class="wordmark__name">Brindlemoor Systems</span>
    </div>
    <p class="web">www.brindlemoor-systems.com</p>
  </section>

  <section class="card card--blue" aria-label="Business card back, blue">
    <div class="wordmark">
      <span class="wordmark__dot"></span>
      <span class="wordmark__name">Brindlemoor Systems</span>
    </div>
    <p class="web">www.brindlemoor-systems.com</p>
  </section>

</main>
</body>
</html>
```